Project Brief for Kids Triathlon Membership and Kids Summer Series Flyer

Objective:
Design a visually engaging double-sided flyer for inclusion in registration bags of participants in the Campus Multisport Quest. The flyer aims to encourage young athletes to redeem their complimentary Kids membership and promote ongoing participation at their local triathlon club or in our exciting Kids Summer Series races, where they will receive a finisher medal. The goal is to motivate participants to collect all three medals and connect them for a complete 'tri-angle' achievement.
Design Requirements:
Format: Double-sided flyer
Size: Standard A4
A fresh and professional design that aligns with the brand guidelines: Pelican Endurance Union Brand Kit
Engaging visuals to appeal to kids and parents alike
Clear call-to-action messages to redeem the free membership and encourage participation in the Summer Series
Key Information to Include:
Membership Offer:
Free Kids membership for all new PelEndurance members, valid for a Standard Non-Club Junior membership.
Emphasize the one-time use code and the deadline for activation (before December 31, 2023).
Inform that the free membership is valid from activation until June 30, 2024.
Include the requirement for Parent/Guardian permission for redemption.
Kids Summer Series Races:
Race 1: Marrow Cove Triathlon (14th December 2024) – Hosted by Bramble Point Triathlon and Multisport
Race 2: Quill Harbour Fun Day (19th January 2025) – Hosted by Triathlon Vista
Race 3: Pinegate Triathlon (23rd February 2025) – Hosted by Wattleford Triathlon Club
Medal Collection:
Highlight the medal collection theme: “Collect all 3 medals to connect and complete the tri-angle.”
Partnership Acknowledgment:
Acknowledge the support of affiliated clubs, Glenhollow, and the Corvalle Authority for making the Kids series possible.
Important Notes (Ts & Cs):
Clearly outline the Terms & Conditions associated with the membership offer:
Offer available to new PelEndurance members only.
Code valid for one-time use only.
Membership activation required by December 31, 2024.
This was on the Ts & Cs last year *Offer available to new PelEndurance members only and only valid for use on a Standard Non-Club Junior membership. Code is valid for one use only. Activate membership before 31st December 2024. Free Membership only valid from date of activation until 30th June 2025. Parent/Guardian permission is required to redeem membership. By activating membership, you accept the Terms & Conditions and Code of Conduct of membership with PelEndurance.
I will forward the code to redeem the free membership to add to the flyer as soon as I receive it.
Look and feel

```html
<!DOCTYPE html>
<html lang="en">
<head>
<meta charset="utf-8">
<title>Kids Triathlon Membership &amp; Summer Series Flyer</title>
<link rel="stylesheet" href="https://fonts.googleapis.com/css2?family=Roboto+Condensed:wght@400;700;800&family=Roboto:wght@400;500;700;900&display=swap">
<style>
:root{
  --stage:#d9dbd7;
  --red:#e3202a;
  --blue:#1c4f9e;
  --sky:#28a9e1;
  --purple:#7d3f98;
  --orange:#f37b2b;
  --yellow:#fdd10f;
  --navy:#2b3191;
  --headline:#ffe600;
  --white:#ffffff;
  --ink:#1d1d1b;
}
*{box-sizing:border-box;margin:0;padding:0}
html,body{width:1200px;height:538px;overflow:hidden;background:var(--stage)}
body{position:relative;font-family:"Roboto",Arial,sans-serif;color:var(--ink)}
.flyer{position:absolute;top:19px;width:354px;height:500px;overflow:hidden;background:var(--white)}
.flyer--front{left:226px;background:var(--red)}
.flyer--back{left:620px}
.shapes{position:absolute;inset:0}

/* front */
.offer-headline{position:absolute;top:14px;left:0;width:100%;text-align:center;color:var(--headline);font-family:"Roboto Condensed",sans-serif;font-weight:700;font-size:21px;line-height:20px}
.title{position:absolute;top:104px;left:0;width:100%;text-align:center;color:var(--white);font-family:"Roboto Condensed",sans-serif;font-weight:800;font-size:56px;line-height:52px;letter-spacing:-.5px}
.subtitle{position:absolute;top:157px;left:0;width:100%;text-align:center;color:var(--white);font-family:"Roboto Condensed",sans-serif;font-weight:700;font-size:20.5px;line-height:24px}
.photo{position:absolute}
.photo--front{top:192px;left:20px;width:318px;height:154px;border-radius:40px 20px 30px 50px;background:linear-gradient(160deg,#8fa3b3 0%,#c9d3dc 45%,#5c6f8a 100%)}
.photo--back{top:0;left:0;width:354px;height:210px;background:linear-gradient(180deg,#b8453f 0%,#6b6f86 35%,#8c98a6 70%,#c7ccd0 100%)}
.medal{position:absolute;top:256px;left:10px;width:80px;height:80px;z-index:3}
.medal__burst{position:absolute;inset:0;width:80px;height:80px}
.medal__text{position:absolute;top:14px;left:8px;width:64px;text-align:center;color:var(--white);font-weight:700;font-size:7px;line-height:8px;transform:rotate(-20deg)}
.medal__text b{display:block;font-size:18px;line-height:18px;font-weight:900}

.series-bar{position:absolute;height:17px;border-radius:8px;background:var(--navy);color:var(--white);font-weight:700;font-size:11.5px;line-height:17px;text-align:center;z-index:2}
.flyer--front .series-bar{top:341px;left:34px;width:286px}
.flyer--back .series-bar{top:230px;left:34px;width:286px}

.races{position:absolute;left:10px;width:334px;display:flex;gap:5px;z-index:2}
.flyer--front .races{top:366px}
.flyer--back .races{top:253px}
.race{position:relative;flex:1;height:80px;padding-top:14px;background:var(--white);border:2px solid var(--blue);border-radius:0 0 8px 8px;text-align:center;font-size:7px;line-height:8.5px}
.race__label{position:absolute;top:-11px;left:50%;transform:translateX(-50%);width:62px;height:17px;border-radius:8px;background:var(--red);color:var(--white);font-weight:700;font-size:11px;line-height:17px}
.race__host{margin-top:4px}
.race__club{margin-top:6px;font-weight:900;font-size:9px;line-height:10px;color:var(--blue)}

.footer{position:absolute;left:0;bottom:0;width:100%;height:48px;background:var(--blue);color:var(--white);text-align:center;padding-top:7px}
.footer__lead{font-weight:500;font-size:12px;line-height:15px}
.footer__contact{font-weight:700;font-size:10.5px;line-height:16px}

/* back */
.offer-card{position:absolute;top:144px;left:11px;width:332px;height:84px;background:var(--white);border:2px solid var(--navy);border-radius:0 0 10px 10px;padding-top:22px;text-align:center;font-weight:700;font-size:7.6px;line-height:10px}
.offer-card__title{position:absolute;top:-14px;left:50%;transform:translateX(-50%);width:246px;height:30px;border-radius:15px;background:var(--red);color:var(--white);font-family:"Roboto Condensed",sans-serif;font-weight:700;font-size:21px;line-height:30px}
.offer-card li{list-style:none}
.offer-card li::before{content:"";display:inline-block;width:3.5px;height:3.5px;border-radius:50%;background:var(--red);margin-right:4px;vertical-align:middle}
.thanks{position:absolute;top:346px;left:0;width:100%;text-align:center;font-weight:700;font-size:8.5px;line-height:11px}
.sponsors{position:absolute;top:374px;left:0;width:100%;display:flex;justify-content:center;align-items:center;gap:26px}
.sponsor{display:flex;align-items:center;gap:5px;font-weight:900;font-size:19px;color:var(--blue)}
.sponsor__mark{width:13px;height:13px;background:var(--yellow)}
.sponsor--gov{color:var(--ink);font-weight:500;font-size:14px;line-height:14px}
.sponsor--gov .sponsor__mark{border-radius:50%;background:var(--navy)}
.terms{position:absolute;top:414px;left:12px;width:330px;text-align:center;color:#666;font-size:5.2px;line-height:6.6px}
</style>
</head>
<body>

<section class="flyer flyer--front" aria-label="Flyer front">
  <svg class="shapes" viewBox="0 0 354 500" aria-hidden="true">
    <path d="M0 0H120C100 20 60 30 40 50 25 65 10 70 0 72Z" fill="var(--blue)"/>
    <path d="M130 0H240C225 8 190 10 160 8 145 6 135 4 130 0Z" fill="var(--blue)"/>
    <path d="M0 108C60 98 120 112 190 96 250 84 310 90 354 84V210H0Z" fill="var(--sky)"/>
    <path d="M260 200C300 205 330 190 354 192V470H270Z" fill="var(--purple)"/>
    <path d="M0 250C30 240 50 260 70 270V470H0Z" fill="var(--orange)"/>
    <path d="M240 400C290 395 320 410 354 398V470H240Z" fill="var(--yellow)"/>
  </svg>

  <p class="offer-headline">Free Kids membership for all new<br>PelEndurance members,<br>valid for a<br>Standard Non-Club Junior membership</p>
  <h1 class="title">Kids Triathlon</h1>
  <p class="subtitle">Membership &amp; Summer Series Races</p>

  <div class="photo photo--front" role="img" aria-label="Photo of young swimmers in caps running out of the sea at a kids triathlon start"></div>

  <div class="medal">
    <svg class="medal__burst" viewBox="0 0 80 80" aria-hidden="true">
      <circle cx="40" cy="40" r="33" fill="var(--red)"/>
      <circle cx="40" cy="40" r="35.5" fill="none" stroke="var(--red)" stroke-width="7" stroke-dasharray="4 3.2"/>
    </svg>
    <p class="medal__text">Collect all<b>3</b>medals to connect and complete the tri-angle</p>
  </div>

  <h2 class="series-bar">Kids Summer Series Races:</h2>
  <div class="races">
    <article class="race"><span class="race__label">Race 1</span>Marrow Cove Triathlon<br>(14th December 2024)<p class="race__host">Hosted by</p><p class="race__club">Bramble Point</p></article>
    <article class="race"><span class="race__label">Race 2</span>Quill Harbour Fun Day<br>19th January 2025)<br>Hosted by<p class="race__club">Triathlon Vista</p></article>
    <article class="race"><span class="race__label">Race 3</span>Pinegate Triathlon<br>(23rd February 2025)<br>Hosted by<p class="race__club">Wattleford Triathlon Club</p></article>
  </div>

  <footer class="footer">
    <p class="footer__lead">For more informations</p>
    <p class="footer__contact">www.pelicanendurance.org | jo.marlow@pelicanendurance.org</p>
  </footer>
</section>

<section class="flyer flyer--back" aria-label="Flyer back">
  <div class="photo photo--back" role="img" aria-label="Photo of a crowd of kids running into the sea at a beach triathlon with event tents behind"></div>

  <div class="offer-card">
    <h2 class="offer-card__title">Membership Offer:</h2>
    <ul>
      <li>Free Kids membership for all new PelEndurance members,<br>valid for a Standard Non-Club Junior membership.</li>
      <li>One-time use code and the deadline for activation (before December 31, 2023).</li>
      <li>Free membership is valid from activation until June 30, 2024.</li>
      <li>Parent/Guardian permission for redemption.</li>
    </ul>
  </div>

  <h2 class="series-bar">Kids Summer Series Races:</h2>
  <div class="races">
    <article class="race"><span class="race__label">Race 1</span>Marrow Cove Triathlon<br>(14th December 2024)<p class="race__host">Hosted by</p><p class="race__club">Bramble Point</p></article>
    <article class="race"><span class="race__label">Race 2</span>Quill Harbour Fun Day<br>19th January 2025)<br>Hosted by<p class="race__club">Triathlon Vista</p></article>
    <article class="race"><span class="race__label">Race 3</span>Pinegate Triathlon<br>(23rd February 2025)<br>Hosted by<p class="race__club">Wattleford Triathlon Club</p></article>
  </div>

  <p class="thanks">We are thankful for the support of<br>Kids Summer Series Races make happened possible !</p>
  <div class="sponsors">
    <span class="sponsor"><span class="sponsor__mark"></span>Glenhollow</span>
    <span class="sponsor sponsor--gov"><span class="sponsor__mark"></span>Corvalle<br>Authority</span>
  </div>

  <p class="terms">*Offer available to new PelEndurance members only and only valid for use on a Standard Non-Club Junior membership. Code is valid for one use only. Activate membership before 31st December 2024. Free Membership only valid from date of activation until 30th June 2025. Parent/Guardian permission is required to redeem membership. By activating membership, you accept the Terms &amp; Conditions and Code of Conduct of membership with PelEndurance.</p>

  <footer class="footer">
    <p class="footer__lead">For more informations</p>
    <p class="footer__contact">www.pelicanendurance.org | jo.marlow@pelicanendurance.org</p>
  </footer>
</section>

</body>
</html>
```